Updated Business Cards

We need to update our business cards to reflect new services and employees. We are a luxury vacation rental company in Sandpoint, Idaho. Would also like to make the front facing font easier to read (larger fonts) I love the original logo created for our company and want to use this for the back of the business card created like before - with the dark blue color. See previous files.

Front of the card needs to include:
Employee Name
Title
Phone: 555-555-0147 (ext X)
Address: 417 W. Maple St, Ste 6
Alder Cove, WY 83799
Book Direct: www.RestLakeview.example

```html
<!DOCTYPE html>
<html lang="en">
<head>
<meta charset="utf-8">
<title>Harlow Stays – Business Card</title>
<link href="https://fonts.googleapis.com/css2?family=Open+Sans:wght@300;400;600;700&display=swap" rel="stylesheet">
<style>
  :root {
    --navy: #072c5e;
    --paper: #ffffff;
    --backdrop: #adadad;
    --body-text: #555555;
    --rule: #9a9a9a;
  }
  * { margin: 0; padding: 0; box-sizing: border-box; }
  html, body { width: 1200px; height: 1000px; overflow: hidden; }
  body {
    background: var(--backdrop);
    font-family: "Open Sans", Arial, sans-serif;
    position: relative;
  }
  .card {
    position: absolute;
    left: 293px;
    width: 615px;
    height: 354px;
    box-shadow: 8px 10px 14px rgba(0,0,0,0.28);
  }
  .card-front { top: 96px; background: var(--paper); }
  .card-back { top: 509px; background: var(--navy); }

  .brand {
    position: absolute;
    left: 0; width: 307px; top: 130px;
    display: flex; align-items: center; justify-content: center; gap: 12px;
  }
  .brand-square { width: 22px; height: 22px; background: var(--navy); }
  .brand-name {
    color: var(--navy);
    font-weight: 600;
    font-size: 30px;
    letter-spacing: 0.5px;
  }
  .divider {
    position: absolute;
    left: 307px; top: 79px;
    width: 2px; height: 157px;
    background: var(--rule);
  }
  .contact { position: absolute; left: 340px; top: 82px; }
  .employee-name {
    color: var(--navy); font-weight: 700; font-size: 18px; letter-spacing: 0.6px; line-height: 23px;
  }
  .employee-title {
    color: var(--navy); font-size: 18px; line-height: 23px; letter-spacing: 0.3px;
  }
  .contact-line {
    display: flex; align-items: flex-start; gap: 14px;
    color: var(--body-text); font-size: 18px; line-height: 20px;
  }
  .contact-line svg { flex: none; fill: var(--navy); margin-top: 3px; }
  .phone-line { margin-top: 18px; }
  .address-line { margin-top: 20px; }
  .address-line svg { margin-top: 10px; }

  .book-band {
    position: absolute; left: 0; bottom: 0;
    width: 100%; height: 80px;
    background: var(--navy); color: var(--paper);
    text-align: center;
  }
  .book-label { font-weight: 700; font-size: 18px; padding-top: 10px; line-height: 23px; }
  .book-url { font-size: 25px; line-height: 32px; font-weight: 300; }
  .book-url strong { font-weight: 700; }

  .back-brand {
    position: absolute; inset: 0;
    display: flex; align-items: center; justify-content: center; gap: 22px;
  }
  .back-brand .brand-square { width: 44px; height: 44px; background: var(--paper); }
  .back-brand .brand-name { color: var(--paper); font-size: 62px; }
</style>
</head>
<body>
  <section class="card card-front">
    <div class="brand">
      <span class="brand-square"></span>
      <span class="brand-name">Harlow Stays</span>
    </div>
    <div class="divider"></div>
    <div class="contact">
      <div class="employee-name">EMPLOYEE NAME</div>
      <div class="employee-title">TITLE</div>
      <div class="contact-line phone-line">
        <svg width="14" height="14" viewBox="0 0 24 24" aria-hidden="true"><path d="M6.6 10.8a15.1 15.1 0 0 0 6.6 6.6l2.2-2.2a1 1 0 0 1 1-.25 11.4 11.4 0 0 0 3.6.57 1 1 0 0 1 1 1V20a1 1 0 0 1-1 1A17 17 0 0 1 3 4a1 1 0 0 1 1-1h3.5a1 1 0 0 1 1 1c0 1.25.2 2.45.57 3.57a1 1 0 0 1-.25 1z"/></svg>
        <span>555-555-0147 (ext X)</span>
      </div>
      <div class="contact-line address-line">
        <svg width="14" height="18" viewBox="0 0 14 18" aria-hidden="true"><path d="M7 0a7 7 0 0 0-7 7c0 5 7 11 7 11s7-6 7-11a7 7 0 0 0-7-7zm0 9.3A2.3 2.3 0 1 1 7 4.7a2.3 2.3 0 0 1 0 4.6z"/></svg>
        <span>417 W. Maple St, Ste 6<br>Alder Cove, WY 83799</span>
      </div>
    </div>
    <div class="book-band">
      <div class="book-label">BOOK DIRECT:</div>
      <div class="book-url"><strong>RestLakeview</strong>.example</div>
    </div>
  </section>

  <section class="card card-back">
    <div class="back-brand">
      <span class="brand-square"></span>
      <span class="brand-name">Harlow Stays</span>
    </div>
  </section>
</body>
</html>
```